Eye-catching Yellow Page Ad for Attorney's Office

We need a phone book advertisement for our law office. We practice workers' compensation law, and our clientele consists exclusively of individuals who have been injured on the job. The dimensions of the print ad will be 6" W X 4.54" H.

We've had our current ad for several years, and wanted to get a new one that has been designed by a professional. Being that it's an ad for a law firm, it needs to be professional looking, but we're hoping to have something that looks a little more modern and has eye-catching appeal. We like the text that is included in the ad, and we want to make sure our phone number is very visible. No real preference for color scheme.

I've attached a copy of our current ad. All the information included in there is accurate. Our office name is Thornbury & Lisle, PLLC. The ethical rules for attorney advertising require the PLLC to be included in the ad, but it can be smaller than the other text (see our current ad).

Target Market(s)

Our potential clients are injured workers looking for legal representation in their workers' compensation claim.

Industry/Entity Type

Attorney

Font styles to use
Serif
Sans Serif

Requirements
Must have
• Professional, but stands out from the crowd
Nice to have
• Clean modern design
Should not have
• We don't want it to be too crowded or over-worked.

```html
<!DOCTYPE html>
<html lang="en">
<head>
<meta charset="utf-8">
<title>Thornbury &amp; Lisle, PLLC — Workers' Compensation Ad</title>
<link rel="stylesheet" href="https://fonts.googleapis.com/css2?family=Marcellus+SC&family=Open+Sans:wght@400;600&display=swap">
<style>
  :root {
    --ink: #1c1c1c;
    --gold: #a8962f;
    --wine: #8e0f3b;
    --slate: #545454;
    --paper: #ffffff;
    --backdrop: #ececec;
    --muted: #444444;
  }
  * { margin: 0; padding: 0; box-sizing: border-box; }
  html, body { width: 1200px; height: 1000px; overflow: hidden; background: var(--backdrop); }
  .ad {
    position: absolute; left: 50px; top: 84px; width: 1100px; height: 832px;
    background: var(--paper); overflow: hidden;
    box-shadow: 0 10px 30px rgba(0,0,0,.35);
    font-family: "Marcellus SC", "Times New Roman", serif;
    color: var(--ink);
  }
  .ad-swoosh { position: absolute; inset: 0; }
  .headline {
    position: absolute; top: 18px; left: 0; width: 1110px; text-align: center;
    font-size: 36px; font-weight: 400; letter-spacing: 7px;
  }
  .tagline {
    position: absolute; top: 68px; left: 0; width: 1110px; text-align: center;
    font-size: 21px; letter-spacing: 1.5px; color: var(--gold);
  }
  .phone {
    position: absolute; top: 96px; left: 0; width: 1110px; text-align: center;
    font-family: "Open Sans", Arial, sans-serif; font-size: 84px; color: var(--wine);
    letter-spacing: 2px; line-height: 1.2;
  }
  .phone strong { font-weight: 600; }
  .gavel {
    position: absolute; top: 58px; left: 945px; width: 150px; height: 140px;
    background: radial-gradient(ellipse at 50% 55%, #8a5a2c 0%, #5e3817 60%, rgba(255,255,255,0) 72%);
  }
  .promise {
    position: absolute; top: 198px; left: 0; width: 1100px; text-align: center;
    font-size: 24px; letter-spacing: 1.5px; line-height: 37px;
  }
  .promise em { font-style: normal; color: var(--wine); }
  .values {
    position: absolute; top: 282px; right: 56px;
    font-family: "Open Sans", Arial, sans-serif; font-size: 21px; letter-spacing: 2px;
    color: var(--gold); text-transform: uppercase;
  }
  .values .dot { margin: 0 12px; }
  .portrait {
    position: absolute; left: 22px; top: 277px; width: 383px; height: 350px;
    background: linear-gradient(160deg, #7a5a3a 0%, #4a3626 55%, #2e2620 100%);
    box-shadow: 0 4px 12px rgba(0,0,0,.45);
    border: 3px solid #f4f4f4;
  }
  .portrait-names {
    position: absolute; left: 0; right: 0; bottom: 12px; display: flex; justify-content: space-around;
    font-family: "Open Sans", Arial, sans-serif; font-weight: 600; font-size: 18px; color: #fff;
    text-shadow: 0 1px 3px #000;
  }
  .services { position: absolute; left: 488px; top: 332px; }
  .services h2 { font-weight: 400; font-size: 25px; letter-spacing: 2px; color: var(--muted); margin-bottom: 10px; }
  .services ul { list-style: none; font-size: 15px; letter-spacing: 1px; color: var(--muted); }
  .services li { line-height: 22px; padding-left: 24px; position: relative; }
  .services li::before { content: ""; position: absolute; left: 0; top: 11px; width: 13px; border-top: 1px solid #888; }
  .firm {
    position: absolute; top: 688px; left: 0; width: 1100px; text-align: center;
    font-size: 72px; letter-spacing: 3px; color: var(--gold); line-height: 1;
  }
  .firm-name { position: relative; display: inline-block; }
  .firm-suffix {
    position: absolute; right: 0; top: -26px; font-size: 22px; letter-spacing: 3px; color: #fff; line-height: 1;
  }
  .address, .web {
    position: absolute; left: 0; width: 1100px; text-align: center; color: #fff; letter-spacing: 3px;
  }
  .address { top: 766px; font-size: 21px; }
  .web { top: 800px; font-size: 18px; }
</style>
</head>
<body>
  <section class="ad" aria-label="Thornbury &amp; Lisle workers' compensation advertisement">
    <svg class="ad-swoosh" viewBox="0 0 1100 832" aria-hidden="true">
      <path d="M0 832 L0 668 C500 664 900 596 1100 346 L1100 832 Z" fill="var(--slate)"/>
      <path d="M0 656 C500 650 900 560 1100 300 L1100 350 C900 600 500 666 0 670 Z" fill="var(--wine)"/>
    </svg>

    <h1 class="headline">Workers' Compensation</h1>
    <p class="tagline">Former Assistant Attorneys General Who Know The System</p>
    <p class="phone">360 <strong>555-0147</strong></p>
    <div class="gavel" role="img" aria-label="Illustration of a wooden judge's gavel and sound block"></div>

    <p class="promise">At Thornbury &amp; Lisle, We Provide Personal Attention To Our Clients.<br>
      That Means Your Case Is Handled By An Attorney, <em>Not An Assistant.</em></p>
    <p class="values">Professional<span class="dot">•</span>Committed<span class="dot">•</span>Effective</p>

    <div class="portrait" role="img" aria-label="Photograph of the two attorneys standing in a law library holding a book">
      <div class="portrait-names"><span>Owen Thornbury</span><span>Clara Lisle</span></div>
    </div>

    <div class="services">
      <h2>We Can Help With:</h2>
      <ul>
        <li>Workplace Injuries Or Death</li>
        <li>Lost Wages</li>
        <li>Medical Expenses &amp; Treatment</li>
        <li>Hearing Loss Claims</li>
        <li>Pension Claims</li>
        <li>Disability Awards</li>
        <li>Return To Work Issues</li>
      </ul>
    </div>

    <p class="firm"><span class="firm-name">Thornbury &amp; Lisle<span class="firm-suffix">PLLC</span></span></p>
    <p class="address">482 W. Harbor Suite 310, Larkport</p>
    <p class="web">www.thornburylisle.com</p>
  </section>
</body>
</html>
```